Our new beauty salon requires a price list brochure

Our beauty clinic is a medical grade skin care clinic. So our salon is very clinical and professional in appearance. I would like the colours to be similar to our logo design with some nice texture or abstract shapes thrown in.
Pricelist, contact details and logo is attached
I would prefer it to be a 3 fold brochure.

Target Market(s)

Females aged 30-50

Colors
85acd3
cedeed
c4c4c4
5c5c5c
000000
ffffff
eea3c7
f9d9e8
dbdbdb

Requirements
Must have
• easy to read

```html
<!DOCTYPE html>
<html lang="en">
<head>
<meta charset="utf-8">
<title>Lumen Aesthetics – Price List Brochure</title>
<link href="https://fonts.googleapis.com/css2?family=Open+Sans:wght@300;400;600&display=swap" rel="stylesheet">
<style>
  :root{
    --slate:#5b7492;
    --slate-deep:#4d6480;
    --sky:#85acd3;
    --mist:#cedeed;
    --silver:#c4c4c4;
    --cloud:#dbdbdb;
    --ink:#5c5c5c;
    --white:#ffffff;
    --blush:#f9d9e8;
    --rose:#eea3c7;
    --stage:#e4e4e4;
  }
  *{box-sizing:border-box;margin:0;padding:0}
  html,body{width:1200px;height:2400px;overflow:hidden}
  body{
    background:var(--stage);
    font-family:"Open Sans",Arial,sans-serif;
    color:var(--ink);
    display:flex;flex-direction:column;align-items:center;justify-content:center;gap:200px;
  }
  .spread{display:flex;width:1080px;height:764px;box-shadow:0 18px 40px rgba(0,0,0,.18)}
  .panel{position:relative;width:360px;height:764px;overflow:hidden;background:var(--white)}
  .panel--slate{background:linear-gradient(180deg,var(--slate) 0%,var(--slate-deep) 100%);color:var(--white)}
  .panel + .panel{border-left:1px solid rgba(0,0,0,.06)}

  .heading{font-weight:400;font-size:26px;color:var(--sky);letter-spacing:.3px;margin-bottom:10px}
  .pill{
    display:inline-block;padding:5px 40px 5px 18px;border-radius:0 20px 20px 0;
    background:var(--mist);color:var(--slate);font-size:20px;font-weight:400;margin-bottom:12px
  }
  .pill--flush{margin-left:-28px;padding-left:28px}
  .price-list{list-style:none;font-size:13px;line-height:1.62}
  .price-list li{display:flex;align-items:baseline;gap:4px}
  .price-list .leader{flex:1;border-bottom:1px dotted currentColor;opacity:.55;transform:translateY(-3px)}
  .price-list .price{white-space:nowrap}
  .sub-title{font-size:11px;font-weight:600;letter-spacing:.6px;margin:10px 0 2px}
  .note{font-size:12px;line-height:1.5}

  .photo{position:absolute;background:linear-gradient(135deg,#f4efec 0%,#e3d2c7 55%,#c9b3a5 100%)}
  .photo--cool{background:linear-gradient(135deg,#f5f6f8 0%,#dfe4ea 60%,#c7cfd8 100%)}
  .photo--round{border-radius:50%;border:5px solid var(--mist)}

  /* Outside spread */
  .fillers{padding:0}
  .fillers__top{padding:24px 28px 0}
  .fillers__price{font-size:14px;margin:-4px 0 10px}
  .fillers__bottom{position:absolute;left:0;right:0;bottom:0;height:300px;padding:80px 28px 0;color:var(--white)}
  .fillers__bottom svg{position:absolute;left:0;top:0}
  .fillers__bottom .note{position:relative}
  .fillers__bottom strong{font-weight:600;display:block;margin-top:6px}

  .waxing{padding:26px 28px 0}
  .waxing__photo{left:0;right:0;top:420px;height:170px}
  .waxing__mens{position:absolute;left:28px;right:28px;top:606px}
  .waxing .extras{margin-top:8px}

  .cover__svg{position:absolute;inset:0}
  .brand{position:absolute;left:0;right:0;top:34px;text-align:center}
  .brand__name{font-weight:300;font-size:42px;color:var(--ink);letter-spacing:2px;text-transform:lowercase;display:inline-flex;align-items:center;gap:12px}
  .brand__dot{width:12px;height:12px;border-radius:50%;background:var(--sky)}
  .brand__sub{font-weight:300;font-size:13px;letter-spacing:6px;color:var(--ink);margin-top:2px}
  .cover__tagline{position:absolute;left:30px;right:30px;bottom:118px;font-size:17px;letter-spacing:.8px;color:var(--white)}
  .cover__web{position:absolute;left:30px;right:30px;bottom:70px;font-size:16px;color:var(--white);letter-spacing:.4px}

  /* Inside spread */
  .ipl-hair{padding:30px 28px 0}
  .ipl-hair .price-list{font-size:13.4px;line-height:1.56}
  .ipl-hair__photo{position:absolute;left:0;bottom:0;width:360px;height:190px}
  .ipl-hair__arc{position:absolute;left:0;bottom:150px}

  .treatments__photo{left:0;right:0;top:0;height:180px}
  .treatments__inset{left:222px;top:118px;width:104px;height:104px}
  .treatments__body{position:absolute;left:28px;right:28px;top:236px}
  .treatments__body .pill{margin-top:8px}
</style>
</head>
<body>

<!-- Outside of brochure -->
<section class="spread spread--outside">
  <article class="panel fillers">
    <div class="fillers__top">
      <div class="pill pill--flush">Dermal Fillers &amp; Lip Fillers</div>
      <p class="fillers__price">$500 per ml</p>
      <p class="sub-title">CHEMICAL PEELS</p>
      <ul class="price-list">
        <li><span>Lactic acid peel</span><span class="leader"></span><span class="price">$90</span></li>
        <li><span>Glycolic acid peel</span><span class="leader"></span><span class="price">$110</span></li>
        <li><span>Salicylic peel</span><span class="leader"></span><span class="price">$120</span></li>
        <li><span>Combination peel</span><span class="leader"></span><span class="price">$130</span></li>
        <li><span>Deep renewal peel</span><span class="leader"></span><span class="price">$150</span></li>
      </ul>
      <ul class="price-list extras" style="margin-top:10px">
        <li><span>Enzyme peel</span><span class="leader"></span><span class="price">$120</span></li>
        <li><span>Brightening peel</span><span class="leader"></span><span class="price">$130</span></li>
        <li><span>Retinol peel</span><span class="leader"></span><span class="price">$125</span></li>
        <li><span>Vitamin C peel</span><span class="leader"></span><span class="price">$200</span></li>
      </ul>
    </div>
    <div class="photo photo--round" role="img" aria-label="Portrait photo of a client with clear skin" style="left:38px;top:440px;width:100px;height:100px;z-index:2"></div>
    <div class="photo photo--round" role="img" aria-label="Portrait photo of a client receiving skin care" style="left:146px;top:430px;width:100px;height:100px;z-index:2"></div>
    <div class="fillers__bottom">
      <svg width="360" height="300" viewBox="0 0 360 300" aria-hidden="true">
        <path d="M0 60 Q180 -10 360 30 V300 H0 Z" fill="var(--slate)"/>
        <path d="M0 54 Q180 -16 360 24" fill="none" stroke="var(--mist)" stroke-width="3"/>
      </svg>
      <p class="note"><strong>Skin Booster LED</strong>$80 per session, course of six $420</p>
      <p class="note"><strong>Collagen Microneedling</strong>$250 face, neck and decolletage $350</p>
      <p class="note"><strong>Hydrating Facial</strong>$120 with mask and massage</p>
    </div>
  </article>

  <article class="panel waxing">
    <h2 class="heading">Waxing</h2>
    <ul class="price-list">
      <li><span>Eyebrow</span><span class="leader"></span><span class="price">$20</span></li>
      <li><span>Lip</span><span class="leader"></span><span class="price">$15</span></li>
      <li><span>Chin</span><span class="leader"></span><span class="price">$15</span></li>
      <li><span>Sides of face</span><span class="leader"></span><span class="price">$20</span></li>
      <li><span>Underarm</span><span class="leader"></span><span class="price">$20</span></li>
      <li><span>Full arm</span><span class="leader"></span><span class="price">$40</span></li>
      <li><span>Half arm</span><span class="leader"></span><span class="price">$30</span></li>
      <li><span>Lower leg</span><span class="leader"></span><span class="price">$35</span></li>
      <li><span>Upper leg</span><span class="leader"></span><span class="price">$35</span></li>
      <li><span>Full leg</span><span class="leader"></span><span class="price">$60</span></li>
      <li><span>Inner thigh</span><span class="leader"></span><span class="price">$20</span></li>
      <li><span>Bikini</span><span class="leader"></span><span class="price">$25</span></li>
      <li><span>G String</span><span class="leader"></span><span class="price">$40</span></li>
      <li><span>Brazilian</span><span class="leader"></span><span class="price">$55</span></li>
    </ul>
    <ul class="price-list extras">
      <li><span>Eyebrow wax and lip wax</span><span class="leader"></span><span class="price">$30</span></li>
      <li><span>Eyebrow, lip and chin wax</span><span class="leader"></span><span class="price">$40</span></li>
    </ul>
    <div class="photo photo--cool waxing__photo" role="img" aria-label="Photo of a woman seated on white linen holding a flower"></div>
    <div class="waxing__mens">
      <h2 class="heading">Mens waxing</h2>
      <ul class="price-list">
        <li><span>Mono brow</span><span class="leader"></span><span class="price">$5</span></li>
        <li><span>Eyebrow</span><span class="leader"></span><span class="price">$25</span></li>
        <li><span>Neck</span><span class="leader"></span><span class="price">$20</span></li>
        <li><span>Full back</span><span class="leader"></span><span class="price">$40</span></li>
        <li><span>Chest and Abdomen</span><span class="leader"></span><span class="price">$40</span></li>
      </ul>
    </div>
  </article>

  <article class="panel panel--slate cover">
    <svg class="cover__svg" width="360" height="764" viewBox="0 0 360 764" aria-hidden="true">
      <defs>
        <linearGradient id="coverPhoto" x1="0" y1="0" x2="1" y2="1">
          <stop offset="0" stop-color="#f6f1ee"/>
          <stop offset=".55" stop-color="#e2cfc4"/>
          <stop offset="1" stop-color="#b89a88"/>
        </linearGradient>
      </defs>
      <g role="img" aria-label="Portrait photo of a woman with long brown hair">
        <path d="M0 120 H360 V500 Q300 560 0 540 Z" fill="url(#coverPhoto)"/>
      </g>
      <path d="M0 0 H360 V128 Q180 190 0 150 Z" fill="var(--white)"/>
      <path d="M0 150 Q180 190 360 128" fill="none" stroke="var(--slate)" stroke-width="6"/>
      <path d="M0 548 Q300 568 360 508" fill="none" stroke="var(--silver)" stroke-width="7"/>
    </svg>
    <div class="brand">
      <div class="brand__name"><span class="brand__dot"></span>lumen</div>
      <div class="brand__sub">AESTHETICS</div>
    </div>
    <p class="cover__tagline">MEDICAL GRADE SKIN CARE CLINIC</p>
    <p class="cover__web">www.lumenaesthetics.com.au</p>
  </article>
</section>

<!-- Inside of brochure -->
<section class="spread spread--inside">
  <article class="panel panel--slate ipl-hair">
    <div class="pill pill--flush">IPL hair removal</div>
    <ul class="price-list">
      <li><span>Upper lip</span><span class="leader"></span><span class="price">$50</span></li>
      <li><span>Chin</span><span class="leader"></span><span class="price">$50</span></li>
      <li><span>Cheeks</span><span class="leader"></span><span class="price">$70</span></li>
      <li><span>Whole face</span><span class="leader"></span><span class="price">$150</span></li>
      <li><span>Bikini</span><span class="leader"></span><span class="price">$100</span></li>
      <li><span>G String</span><span class="leader"></span><span class="price">$130</span></li>
      <li><span>Brazilian</span><span class="leader"></span><span class="price">$180</span></li>
      <li><span>Underarms</span><span class="leader"></span><span class="price">$90</span></li>
      <li><span>Half arm</span><span class="leader"></span><span class="price">$150</span></li>
      <li><span>Full arm</span><span class="leader"></span><span class="price">$250</span></li>
      <li><span>Half leg</span><span class="leader"></span><span class="price">$200</span></li>
      <li><span>Thighs</span><span class="leader"></span><span class="price">$200</span></li>
      <li><span>Full leg</span><span class="leader"></span><span class="price">$380</span></li>
      <li><span>Half back</span><span class="leader"></span><span class="price">$180</span></li>
      <li><span>Full back</span><span class="leader"></span><span class="price">$300</span></li>
      <li><span>Shoulders</span><span class="leader"></span><span class="price">$150</span></li>
      <li><span>Nipples</span><span class="leader"></span><span class="price">$50</span></li>
      <li><span>Snail trail</span><span class="leader"></span><span class="price">$60</span></li>
    </ul>
    <svg class="ipl-hair__arc" width="360" height="60" viewBox="0 0 360 60" aria-hidden="true">
      <path d="M0 60 Q150 0 360 30 V60 Z" fill="var(--white)"/>
      <path d="M0 56 Q150 -4 360 26" fill="none" stroke="var(--mist)" stroke-width="3"/>
    </svg>
    <div class="photo photo--cool ipl-hair__photo" role="img" aria-label="Photo of an IPL hair removal treatment on a client's underarm"></div>
  </article>

  <article class="panel waxing">
    <h2 class="heading">Waxing</h2>
    <ul class="price-list">
      <li><span>Eyebrow</span><span class="leader"></span><span class="price">$20</span></li>
      <li><span>Lip</span><span class="leader"></span><span class="price">$15</span></li>
      <li><span>Chin</span><span class="leader"></span><span class="price">$15</span></li>
      <li><span>Sides of face</span><span class="leader"></span><span class="price">$20</span></li>
      <li><span>Underarm</span><span class="leader"></span><span class="price">$20</span></li>
      <li><span>Full arm</span><span class="leader"></span><span class="price">$40</span></li>
      <li><span>Half arm</span><span class="leader"></span><span class="price">$30</span></li>
      <li><span>Lower leg</span><span class="leader"></span><span class="price">$35</span></li>
      <li><span>Upper leg</span><span class="leader"></span><span class="price">$35</span></li>
      <li><span>Full leg</span><span class="leader"></span><span class="price">$60</span></li>
      <li><span>Inner thigh</span><span class="leader"></span><span class="price">$20</span></li>
      <li><span>Bikini</span><span class="leader"></span><span class="price">$25</span></li>
      <li><span>G String</span><span class="leader"></span><span class="price">$40</span></li>
      <li><span>Brazilian</span><span class="leader"></span><span class="price">$55</span></li>
    </ul>
    <ul class="price-list extras">
      <li><span>Eyebrow wax and lip wax</span><span class="leader"></span><span class="price">$30</span></li>
      <li><span>Eyebrow, lip and chin wax</span><span class="leader"></span><span class="price">$40</span></li>
    </ul>
    <div class="photo photo--cool waxing__photo" role="img" aria-label="Photo of a woman seated on white linen holding a flower"></div>
    <div class="waxing__mens">
      <h2 class="heading">Mens waxing</h2>
      <ul class="price-list">
        <li><span>Mono brow</span><span class="leader"></span><span class="price">$5</span></li>
        <li><span>Eyebrow</span><span class="leader"></span><span class="price">$25</span></li>
        <li><span>Neck</span><span class="leader"></span><span class="price">$20</span></li>
        <li><span>Full back</span><span class="leader"></span><span class="price">$40</span></li>
        <li><span>Chest and Abdomen</span><span class="leader"></span><span class="price">$40</span></li>
      </ul>
    </div>
  </article>

  <article class="panel panel--slate treatments">
    <div class="photo treatments__photo" role="img" aria-label="Photo of a woman relaxing during a facial treatment"></div>
    <svg style="position:absolute;left:0;top:150px" width="360" height="60" viewBox="0 0 360 60" aria-hidden="true">
      <path d="M0 0 Q200 60 360 20 V60 H0 Z" fill="var(--slate)"/>
      <path d="M0 4 Q200 64 360 24" fill="none" stroke="var(--mist)" stroke-width="3"/>
    </svg>
    <div class="photo photo--round treatments__inset" role="img" aria-label="Close-up photo of a skin rejuvenation treatment"></div>
    <div class="treatments__body">
      <div class="pill pill--flush">IPL Photo Rejuvenation</div>
      <ul class="price-list">
        <li><span>Full face</span><span class="leader"></span><span class="price">$200</span></li>
        <li><span>Neck</span><span class="leader"></span><span class="price">$150</span></li>
        <li><span>Face, neck and decolletage</span><span class="leader"></span><span class="price">$400</span></li>
        <li><span>Hand treatment</span><span class="leader"></span><span class="price">$90</span></li>
      </ul>
      <div class="pill pill--flush">Tinting</div>
      <ul class="price-list">
        <li><span>Eyelash tint</span><span class="leader"></span><span class="price">$25</span></li>
        <li><span>Lash lift and tint</span><span class="leader"></span><span class="price">$95</span></li>
        <li><span>Eyebrow tint and wax</span><span class="leader"></span><span class="price">$40</span></li>
        <li><span>Eyebrow tint</span><span class="leader"></span><span class="price">$20</span></li>
      </ul>
      <ul class="price-list" style="margin-top:10px">
        <li><span>Skin clinic facial</span><span class="leader"></span><span class="price">$80/60min</span></li>
        <li><span>Deep cleanse facial</span><span class="leader"></span><span class="price">$110/1 hour</span></li>
        <li><span>Microdermabrasion</span><span class="leader"></span><span class="price">$120</span></li>
        <li><span>Skin needling</span><span class="leader"></span><span class="price">$175 per area</span></li>
        <li><span>Cosmetic tattoo removal</span><span class="leader"></span><span class="price">$450</span></li>
        <li><span>Skin tag removal</span><span class="leader"></span><span class="price">$90</span></li>
      </ul>
    </div>
  </article>
</section>

</body>
</html>
```